Redesign Of Flower Delivery Subscription Service Website

I need a revamped website of www.bloom-tessa.com

Please revamp current design using same content....

Target Market(s)

people who buy flowers. Brides, wedding planners, wedding photographer, married man, boyfriend, etc.

Industry/Entity Type

Florist

Number of Pages Required

5+ page

Colors

Designer to choose colors to be used in the design.

Requirements
Must have
• I need a revamped website of www.bloom-tessa.com
• Please revamp current design using same content....
Nice to have
Should not have

```html
<!DOCTYPE html>
<html lang="en">
<head>
<meta charset="utf-8">
<title>Bloom Tessa – Free flowers monthly</title>
<link href="https://fonts.googleapis.com/css2?family=Great+Vibes&family=Montserrat:wght@400;500;600&display=swap" rel="stylesheet">
<style>
:root{
  --green:#8cc63f;
  --ink:#333;
  --text:#555;
  --muted:#777;
  --soft:#f4f5fa;
  --line:#e3e4ea;
  --white:#fff;
}
*{margin:0;padding:0;box-sizing:border-box}
html,body{width:1130px;height:1200px;overflow:hidden;background:var(--white)}
body{position:relative;font-family:'Montserrat',sans-serif;color:var(--text)}
.abs{position:absolute}
/* header */
.site-header{left:0;top:0;width:1130px;height:97px;border-bottom:1px solid #cfd0d6;background:var(--white)}
.call{left:150px;top:46px;font-size:9px;color:var(--muted);display:flex;align-items:center;gap:10px}
.call b{color:var(--ink);font-weight:600}
.brand{left:465px;top:34px;width:200px;text-align:center;font-size:21px;font-weight:400;letter-spacing:1px;color:var(--ink)}
.ornament{top:32px;width:66px;height:36px;background:#ececef;border-radius:18px}
.ornament.left{left:401px}.ornament.right{left:664px}
.search{left:855px;top:47px}
.buy{left:887px;top:36px;width:92px;height:29px;border-radius:15px;background:var(--white);box-shadow:0 3px 12px rgba(0,0,0,.08);display:flex;align-items:center;justify-content:center;gap:6px;color:var(--green);font-size:9px;font-weight:600}
/* nav */
.main-nav{left:0;top:97px;width:1130px;height:49px;background:var(--white);box-shadow:0 6px 10px rgba(0,0,0,.03)}
.main-nav a{position:absolute;top:20px;font-size:9px;color:var(--muted);text-decoration:none;letter-spacing:.2px}
.main-nav a.active{color:#555}
.main-nav .underline{position:absolute;left:565px;top:47px;width:94px;height:2px;background:var(--green)}
/* hero */
.hero{left:0;top:146px;width:1130px;height:219px;background:var(--soft)}
.hero-deco-left{left:0;top:61px;width:196px;height:158px;background:radial-gradient(circle at 80% 45%,#e7b23a 0 18%,transparent 19%),linear-gradient(45deg,#d9b9c8,#e9ecef 60%,transparent);opacity:.85}
.hero-deco-right{left:973px;top:0;width:157px;height:166px;background:radial-gradient(circle at 65% 30%,#f3eee3 0 22%,transparent 23%),linear-gradient(200deg,#3f6b4a,#6a8f6f 60%,transparent 85%);opacity:.85}
.hero-title{left:0;width:1130px;top:83px;text-align:center;font-family:'Great Vibes',cursive;font-size:34px;color:var(--green)}
.crumbs{left:0;width:1130px;top:126px;text-align:center;font-size:11px;color:var(--ink)}
/* content */
.section-title{left:0;width:1130px;top:427px;text-align:center;font-size:14.5px;font-weight:600;color:#444;line-height:18px;letter-spacing:.3px}
.photo{left:362px;top:506px;width:406px;height:186px;background:linear-gradient(90deg,#3a2a2a,#7b6a70 40%,#8a8d96 65%,#e6e2da)}
.copy{left:362px;width:406px;text-align:center;font-size:10px;line-height:17.7px;color:var(--text)}
/* footer */
.site-footer{left:0;top:942px;width:1130px;height:258px;background:var(--soft)}
.f-brand{left:150px;top:984px;font-size:19px;letter-spacing:1px;color:var(--ink)}
.upgrade{left:150px;top:1037px;display:flex;align-items:center;gap:10px;font-size:10px;font-weight:600;color:#444}
.email{left:150px;top:1071px;width:152px;height:26px;background:#e9eaee;font-size:8.5px;color:#666;padding:8px 10px}
.submit{left:302px;top:1071px;width:54px;height:26px;background:var(--green);color:var(--white);font-size:9px;text-align:center;line-height:26px}
.f-head{top:985px;font-size:10px;font-weight:600;color:#444}
.f-list{left:503px;top:1011px;list-style:none;font-size:7.5px;color:#555;line-height:17.7px}
.contact{left:779px;top:1009px;font-size:7.5px;color:#555}
.contact li{list-style:none;display:flex;align-items:center;gap:8px;height:17px}
.social{left:797px;top:1068px;display:flex;gap:10px}
.social span{width:8px;height:8px;border-radius:50%;background:#777;display:block}
.f-rule{left:150px;top:1126px;width:830px;height:1px;background:var(--line)}
.copyright{left:413px;top:1156px;font-size:8.5px;color:#444}
.legal{left:842px;top:1156px;width:138px;text-align:right;font-size:8.5px;color:#444}
</style>
</head>
<body>
<header class="abs site-header">
  <div class="abs call">
    <svg width="12" height="14" viewBox="0 0 12 14" fill="none" stroke="#8cc63f" stroke-width="1.2"><rect x="1" y="1" width="7" height="12" rx="1"/><rect x="6" y="2" width="5" height="4"/><line x1="3" y1="11" x2="6" y2="11"/></svg>
    <span>Call now: <b>555-204-7788</b></span>
  </div>
  <div class="abs ornament left" role="img" aria-label="Decorative swirl ornament"></div>
  <div class="abs brand">Bloom Tessa</div>
  <div class="abs ornament right" role="img" aria-label="Decorative swirl ornament"></div>
  <svg class="abs search" width="14" height="14" viewBox="0 0 14 14" fill="none" stroke="#888" stroke-width="1.2"><circle cx="6" cy="6" r="4.5"/><line x1="9.5" y1="9.5" x2="13" y2="13"/></svg>
  <div class="abs buy">
    <svg width="9" height="11" viewBox="0 0 9 11" fill="none" stroke="#8cc63f" stroke-width="1.1"><rect x="1" y="4" width="7" height="6" rx="1"/><path d="M2.8 4V2.8a1.7 1.7 0 0 1 3.4 0V4"/></svg>
    Buy now
  </div>
</header>

<nav class="abs main-nav">
  <a style="left:152px">Home</a>
  <a style="left:221px">How it works</a>
  <a style="left:316px">Delivry areas</a>
  <a style="left:417px">Franchise</a>
  <a style="left:502px">Blog</a>
  <a class="active" style="left:564px">Free flowers monthly</a>
  <a style="left:698px">Corporate Arrangements</a>
  <a style="left:850px">Help</a>
  <svg style="position:absolute;left:909px;top:18px" width="11" height="13" viewBox="0 0 11 13" fill="none" stroke="#888" stroke-width="1"><circle cx="5.5" cy="4" r="3"/><path d="M1 12.5c0-3 2-4.5 4.5-4.5s4.5 1.5 4.5 4.5z"/></svg>
  <a style="left:928px">My account</a>
  <span class="underline"></span>
</nav>

<section class="abs hero">
  <div class="abs hero-deco-left" role="img" aria-label="Orchid stem and yellow ranunculus"></div>
  <div class="abs hero-deco-right" role="img" aria-label="Bouquet of white roses with fern leaves"></div>
  <h1 class="abs hero-title">Refer 3 and your Flowers are free</h1>
  <p class="abs crumbs">Home / Free flowers monthly</p>
</section>

<h2 class="abs section-title">OUR REFERRAL PROGRAM IS<br>THROUGH THE ROOF!</h2>
<div class="abs photo" role="img" aria-label="Photo of two friends in a café looking at a phone"></div>
<p class="abs copy" style="top:733px">Just refer 3 paying customers to us and every month that 3 of your referrals pay their monthly subscription fee, your flowers will be delivered FREE.</p>
<p class="abs copy" style="top:786px">It really is that simple. When you sign up for our service, we will supply you with your own referral link that you can share with your friends on Sharespace. Your friends simply click the link you shared with them and when they sign up our system will recognize that they were referred from your link. All you have to do is Share, Share, Share away,</p>

<footer class="abs site-footer"></footer>
<div class="abs f-brand">Bloom Tessa</div>
<div class="abs upgrade">
  <svg width="16" height="17" viewBox="0 0 16 17" fill="none" stroke="#555" stroke-width="1.2"><rect x="1" y="6" width="14" height="10"/><path d="M1 6l7 5 7-5"/><path d="M5 5V1M8 5V1M11 5V1"/></svg>
  Receive A Free Upgrade
</div>
<div class="abs email">Your email address</div>
<div class="abs submit">Submit</div>

<h3 class="abs f-head" style="left:503px">More Services</h3>
<ul class="abs f-list">
  <li>- Corporate Arrangements</li>
  <li>- Hotel Arrangements</li>
  <li>- Events</li>
  <li>- Weddings</li>
</ul>

<h3 class="abs f-head" style="left:779px">Contact</h3>
<ul class="abs contact">
  <li><svg width="10" height="11" viewBox="0 0 12 14" fill="none" stroke="#777" stroke-width="1.2"><rect x="1" y="1" width="7" height="12" rx="1"/><rect x="6" y="2" width="5" height="4"/></svg>555-204-7788</li>
  <li><svg width="11" height="8" viewBox="0 0 11 8" fill="none" stroke="#777" stroke-width="1"><rect x=".5" y=".5" width="10" height="7"/><path d="M.5 .5l5 4 5-4"/></svg>Email: support@bloomtessa.com</li>
  <li><svg width="10" height="11" viewBox="0 0 10 11" fill="none" stroke="#777" stroke-width="1"><path d="M5 10S1.5 6.5 1.5 4a3.5 3.5 0 0 1 7 0C8.5 6.5 5 10 5 10z"/><circle cx="5" cy="4" r="1.3"/></svg>418 Alder Crest Road, Lakeview CA 90412</li>
</ul>
<div class="abs social"><span></span><span></span><span></span></div>

<div class="abs f-rule"></div>
<p class="abs copyright">Bloom Tessa - Monthly Flowers Delivery Copyright 2018. All Rights Reserved.</p>
<p class="abs legal">Privacy Policy Terms &amp; Conditions</p>
</body>
</html>
```